Flyer Template Design

I have attached 4 files. I would like a design template that could be used across these documents so that they have a common look and feel. The content of the documents is tested and should not be changed significantly. The images can be changed. I have also attache our logo for color compatibility.
Updates

Need extra days to review

Target Market(s)

Wealthy Christian donors

Font styles to use
Serif
Sans Serif

```html
<!DOCTYPE html>
<html lang="en">
<head>
<meta charset="utf-8">
<title>Flyer Template Set</title>
<link href="https://fonts.googleapis.com/css2?family=Oswald:wght@500;600&family=Montserrat:wght@400;600;700&display=swap" rel="stylesheet">
<style>
:root{
  --navy:#0d3f73;
  --navy-dark:#082c55;
  --blue:#1a5fa3;
  --green:#5bb046;
  --ink:#3a3a3a;
  --band:#e4e4e5;
  --frame:#6b6b6b;
  --canvas:#e9e9ea;
}
*{box-sizing:border-box;margin:0;padding:0}
html,body{width:1030px;height:1200px;overflow:hidden}
body{background:var(--canvas);font-family:"Montserrat",sans-serif;color:var(--ink)}
.flyer{position:absolute;width:358px;height:508px;background:#fff;overflow:hidden}
.flyer-1{left:142px;top:80px}.flyer-2{left:530px;top:80px}
.flyer-3{left:142px;top:613px}.flyer-4{left:530px;top:613px}
.frame{position:absolute;inset:9px;border:1px solid var(--frame);pointer-events:none;z-index:5}
.title-band{position:absolute;left:0;top:22px;width:214px;height:30px}
.title-band svg{position:absolute;inset:0}
.title-band h1{position:absolute;left:22px;top:0;font:500 11.5px/30px "Oswald",sans-serif;color:#fff;letter-spacing:.1px;white-space:nowrap}
.block{position:absolute}
p{font-size:5px;line-height:1.42;margin-bottom:2.5px}
b{font-weight:700}
.photo{position:absolute;border-radius:6px}
.heading{font:500 11px/1.1 "Oswald",sans-serif;color:var(--navy);white-space:nowrap}
.card{position:absolute;top:104px;width:148px;height:150px;background:#efefef;border-radius:9px;overflow:hidden}
.card-head{height:19px;background:var(--navy);color:#fff;font:500 6.5px/19px "Oswald",sans-serif;text-align:center;border-radius:9px 9px 0 0}
.card .photo{position:relative;margin:5px 8px 4px;height:54px;border-radius:0}
.card .copy{padding:0 10px}
.card p{font-size:4.4px}
.grey-band{position:absolute;left:9px;right:9px;background:var(--band)}
.cta{position:absolute;left:31px;right:31px;border:1px solid var(--navy);border-radius:5px;padding:12px 18px 6px;text-align:center}
.cta p{font-size:4.6px;margin:0}
.cta-label{position:absolute;left:0;right:0;top:-4px;display:flex;justify-content:center;align-items:center;gap:0;font:700 5.6px/1 "Montserrat",sans-serif;color:var(--navy-dark)}
.cta-label span{background:#fff;padding:0 6px;white-space:nowrap}
.rule{display:block;width:38px;height:1px;background:var(--navy);position:relative}
.rule.l::after,.rule.r::after{content:"";position:absolute;top:-1.5px;width:4px;height:4px;border-radius:50%;background:var(--navy)}
.rule.l::after{left:-2px}.rule.r::after{right:-2px}
.footer{position:absolute;left:9px;right:9px;bottom:9px;height:59px;background:var(--band)}
.pill{position:absolute;left:47px;top:428px;width:264px;height:26px;border-radius:13px;background:linear-gradient(var(--blue),var(--navy-dark));border:1.5px solid #3f77b4;color:#fff;font:700 6.6px/23px "Montserrat",sans-serif;text-align:center;z-index:3}
.brand{position:absolute;left:48px;bottom:22px;display:flex;align-items:center;gap:7px}
.brand-mark{width:12px;height:12px;background:var(--navy)}
.brand-name{font:700 7.4px/1 "Montserrat",sans-serif;color:var(--navy);white-space:nowrap}
.contact{position:absolute;left:185px;bottom:20px}
.contact small{display:block;font-size:5.4px;color:#333}
.contact a{display:block;font:700 9px/1.3 "Montserrat",sans-serif;color:var(--navy);text-decoration:none}
.split-title{display:flex;align-items:center;gap:6px}
.split-title .stack{font:500 9px/1.05 "Oswald",sans-serif;color:var(--navy-dark);border-right:1.5px solid var(--navy-dark);padding-right:5px;white-space:nowrap}
.split-title p{margin:0}
</style>
</head>
<body>

<section class="flyer flyer-1">
  <div class="frame"></div>
  <div class="title-band"><svg viewBox="0 0 214 30"><polygon points="0,0 200,0 192,30 0,30" fill="#0d3f73"/><polygon points="204,0 210,0 202,30 196,30" fill="#5bb046"/></svg><h1>FINISHING THE GREAT COMMISSION</h1></div>
  <div class="block" style="left:22px;right:22px;top:62px">
    <p>Before Jesus ascended into heaven, He commanded His apostles, “Go and make disciples of all nations.” For more than 2000 years the church has been working to fulfill this “<b>Great Commission</b>,” and much has been accomplished. But now, for the first time in history, our generation has the real opportunity to finish the Great Commission in our lifetimes.</p>
  </div>
  <div class="card" style="left:22px">
    <div class="card-head">IT’S ABOUT NATIONS</div>
    <div class="photo" role="img" aria-label="Portraits of three people from different nations" style="background:linear-gradient(90deg,#7a5a3e,#c0574a 50%,#a9866a)"></div>
    <div class="copy">
      <p>In the Bible, the word “nations” refers to people groups: groups of people who share a common ethnicity, culture, and language.</p>
      <p>So when Jesus said, “Go and make disciples of all nations,” He was telling us to take the gospel to every people group on earth.</p>
      <p>Amazingly, there are about 12,000 of these people groups scattered throughout the world. And the Great Commission commands us to make disciples in every one of them.</p>
    </div>
  </div>
  <div class="card" style="left:187px">
    <div class="card-head">WHERE DO WE STAND?</div>
    <div class="photo" role="img" aria-label="Portraits of two people from unreached groups" style="background:linear-gradient(90deg,#b78a6c,#8d7560 55%,#5b4a3c)"></div>
    <div class="copy">
      <p>Today, there are still about 500 people groups who have never heard the gospel. Most of these groups are small and located in remote, difficult places. These remaining “unengaged” people groups have no known believers.</p>
      <p>But now that we know who and where these groups are, by God’s grace it is possible that we can engage every one of them with the gospel within the next 3 years.</p>
    </div>
  </div>
  <div class="block" style="left:22px;right:22px;top:287px;text-align:center;font:700 7.4px/1 'Montserrat',sans-serif;color:var(--navy)">IN OTHER WORDS, WE CAN FINISH THE GREAT COMMISSION!</div>
  <div class="block split-title" style="left:38px;right:30px;top:300px">
    <div class="stack">HASTENING<br>HIS COMING</div>
    <p>The Bible says that believers “ought to live holy and godly lives, looking for and hastening the coming of the day of God.” It also says that day will not come until the gospel has been preached to “all nations.” So how can hasten the day of his coming? By finishing the work He gave us to do: making disciples in all nations.</p>
  </div>
  <div class="cta" style="top:355px;height:49px">
    <div class="cta-label"><i class="rule l"></i><span>YOU CAN MAKE THAT HAPPEN</span><i class="rule r"></i></div>
    <p>Partner with Harvest Reach Partners and finance the missionaries who are taking the gospel for the first time to those last remaining people groups. Your investment will “<b>hasten the coming of the day of God</b>” by accelerating the effort to make “<b>disciples in every nation.</b>” In 2018, our partners helped take the gospel to 231 people groups in 35 countries.</p>
  </div>
  <div class="footer"><div class="brand"><div class="brand-mark"></div><div class="brand-name">Harvest Reach Partners</div></div><div class="contact"><small>To learn more, email Martin Hale at</small><a>mhale@harvestreach.org.</a></div></div>
  <div class="pill">Join us as we invest to make disciples in “all nations” by 2022</div>
</section>

<section class="flyer flyer-2">
  <div class="frame"></div>
  <div class="title-band"><svg viewBox="0 0 214 30"><polygon points="0,0 200,0 192,30 0,30" fill="#0d3f73"/><polygon points="204,0 210,0 202,30 196,30" fill="#5bb046"/></svg><h1>GOD HEART THE NATION</h1></div>
  <div class="block" style="left:22px;width:160px;top:62px">
    <p>From beginning to end, the Bible reveals God’s heart for “the nations.”</p>
    <p>In <b>Genesis</b>, God promises Abraham, “through your offspring all nations on the earth will be blessed.”</p>
    <p>The <b>Psalms</b> prophesy that “all the nations you have made will come and worship before you, Lord...”</p>
    <p>In <b>Isaiah</b>, God promises the Messiah, “I will make you a light to the nations, that my salvation may reach to the ends of the earth.”</p>
    <p>In <b>Isaiah</b>, God promises the Messiah, “I will make you a light to the nations, that my salvation may reach to the ends of the earth.”</p>
  </div>
  <div class="photo" role="img" aria-label="Grid of six portraits of people from many nations" style="left:197px;top:61px;width:138px;height:101px;border-radius:10px;background:linear-gradient(135deg,#8a5b3e,#c9c2b5 35%,#2d6fae 55%,#c43a32 75%,#6b5846)"></div>
  <div class="block" style="left:22px;right:22px;top:166px">
    <p>Daniel sees “one like a son of man” who “was given authority, glory and sovereign power; all nations and peoples of every language worshiped him.”</p>
    <p>In <b>Matthew</b>, Jesus commands his apostles to “Go and make disciples of all nations.” And he links his return to the completion of that task, saying, “This gospel of the kingdom will be preached in the whole world as a testimony to all nations, and then the end will come.”</p>
    <p>In <b>Revelation</b>, John sees a “great multitude that no one could number, from every nation, from all tribes and peoples and languages, standing before the throne...”</p>
    <p>In the Bible, the word “nations” refers to people groups: groups of people who share a common ethnicity, culture, and language. Amazingly, there are more than 12,000 of these nations scattered around the world—and God has promised that every one of them will be included in His Kingdom.</p>
  </div>
  <div class="grey-band" style="top:264px;height:82px"></div>
  <div class="block heading" style="left:22px;top:270px;font-size:11.5px">FINISHING THE TASK</div>
  <div class="photo" role="img" aria-label="Strip of five portraits of unreached people" style="left:22px;top:291px;width:124px;height:38px;border-radius:0;background:linear-gradient(90deg,#6e5442,#a57d62 40%,#b9a3b8 70%,#d6cfc4)"></div>
  <div class="block" style="left:160px;right:20px;top:275px">
    <p>Today, there are still 500 nations who are not yet represented in God’s Kingdom. No one has ever proclaimed the gospel to these “unengaged” people groups, and there are no believers among them. For these groups, God’s promises have yet to be fulfilled. Most of these groups are small and located in remote, difficult places. But because we now know who and where they are, by God’s grace it is possible that we can engage every one of them with the gospel within the next 3 years.</p>
  </div>
  <div class="cta" style="top:365px;height:49px">
    <div class="cta-label"><i class="rule l"></i><span>YOU CAN MAKE THAT HAPPEN.</span><i class="rule r"></i></div>
    <p>Partner with Harvest Reach Partners and finance the missionaries who are taking the gospel for the first time to those last remaining people groups. Your investment will “hastening the coming of the day of God” by accelerating the effort to make “disciples in every nation.” In 2018, our partners helped take the gospel to 231 people groups in 35 countries.</p>
  </div>
  <div class="footer"><div class="brand"><div class="brand-mark"></div><div class="brand-name">Harvest Reach Partners</div></div><div class="contact"><small>To learn more, email Martin Hale at</small><a>mhale@harvestreach.org.</a></div></div>
  <div class="pill">Join us as we invest to make disciples in “all nations” by 2022</div>
</section>

<section class="flyer flyer-3">
  <div class="frame"></div>
  <div class="title-band"><svg viewBox="0 0 214 30"><polygon points="0,0 200,0 192,30 0,30" fill="#0d3f73"/><polygon points="204,0 210,0 202,30 196,30" fill="#5bb046"/></svg><h1>HASTENING HIS COMING</h1></div>
  <div class="block" style="left:22px;right:22px;top:62px">
    <p>In his second letter, the Apostle Peter asks, what kind of people should believers be? He answers, “We ought to live holy and godly lives, looking for and hastening the coming of the day of God.” But how can we do that? How is it possible to hasten the coming of that day?</p>
  </div>
  <div class="photo" role="img" aria-label="Sunrise breaking through clouds over a misty field" style="left:22px;top:95px;width:148px;height:103px;border-radius:9px;background:linear-gradient(180deg,#5b6f86,#e8c577 45%,#9b8a4a 70%,#3b4a2a)"></div>
  <div class="block" style="left:182px;right:22px;top:101px">
    <div class="heading" style="font-size:11px;margin-bottom:5px">“AND THEN THE END WILL COME”</div>
    <p style="font-size:5.3px">When Jesus’ disciples asked Him,<br>Tell us, what will be the sign of your coming and of the end of the age?</p>
    <p style="font-size:5.3px;margin-top:5px"><b>He replied,</b><br>This gospel of the kingdom will be preached in the whole world as a testimony to all nations, and then the end will come.”</p>
  </div>
  <div class="block split-title" style="left:22px;right:18px;top:212px">
    <div class="heading" style="font-size:11px;border-right:1.5px solid var(--navy-dark);padding-right:5px">WHEN WILL JESUS RETURN?</div>
    <p style="font-weight:700;font-size:5px;color:#222;white-space:nowrap">He said, only after gospel has been preached to “all nations.”</p>
  </div>
  <div class="block" style="left:22px;right:22px;top:232px">
    <p>In the Bible, the word “nations” refers to people groups: groups of people with common ethnicity, culture, and language. Amazingly, there are about 12,000 of these “nations” around the world—and Jesus commanded His church to preach the gospel to all of them!</p>
    <p>Today, there are still 500 people groups without a single believer. No one has ever gone to these remaining “unengaged” groups with the gospel. They do not know the name of Jesus.</p>
  </div>
  <div class="grey-band" style="top:280px;height:24px;text-align:center;font:500 8px/24px 'Oswald',sans-serif;color:#222">AFTER 2000 YEARS, ISN’T IT TIME THAT THEY ALL HEARD?</div>
  <div class="block split-title" style="left:22px;right:22px;top:314px">
    <div class="heading" style="font-size:11px;border-right:1.5px solid var(--navy-dark);padding-right:5px;line-height:1.25">FINISHING<br>THE TASK</div>
    <p>So how can we “hasten the coming of the day of God”? By completing the work Jesus gave us to do! Jesus said He would not return until the gospel is preached to every nation, so that’s what we need to do: take the gospel to all the groups that have never once heard the gospel. Fortunately, we now know who these last groups are and where they are located, by God’s grace it is possible that we can engage all of them with the gospel within the next 3 years.</p>
  </div>
  <div class="cta" style="top:367px;height:49px">
    <div class="cta-label"><i class="rule l"></i><span>YOU CAN MAKE THAT HAPPEN</span><i class="rule r"></i></div>
    <p>Partner with Harvest Reach Partners and finance the missionaries who are taking the gospel for the first time to those last remaining people groups. Your investment will “hasten the coming of the day of God” by accelerating the effort to make “disciples in every nation.” In 2018, our partners helped take the gospel to 231 people groups in 35 countries.</p>
  </div>
  <div class="footer"><div class="brand"><div class="brand-mark"></div><div class="brand-name">Harvest Reach Partners</div></div><div class="contact"><small>To learn more, email Martin Hale at</small><a>mhale@harvestreach.org.</a></div></div>
  <div class="pill">Join us as we invest to make disciples in “all nations” by 2022</div>
</section>

<section class="flyer flyer-4">
  <div class="frame"></div>
  <div class="title-band"><svg viewBox="0 0 214 30"><polygon points="0,0 200,0 192,30 0,30" fill="#0d3f73"/><polygon points="204,0 210,0 202,30 196,30" fill="#5bb046"/></svg><h1>THE FINAL LAP</h1></div>
  <div class="block" style="left:22px;right:22px;top:64px">
    <p>Every four years, the Grand Marathon is run through the streets of the host city. The final lap, though, is always run in the Grand Stadium. At the end of the race, the runners burst into the stadium for the final lap, and the crowd explodes in celebration of a long race well run.</p>
  </div>
  <div class="block" style="left:22px;width:152px;top:95px">
    <p style="text-align:justify">For 2000 years, the church has been running a Marathon, racing to fulfill Jesus’ command to “make disciples of all nations.” But now we’re nearly done: we’ve come into the stadium; we’re on the final lap. And the heavenly crowd is standing and cheering!</p>
  </div>
  <div class="photo" role="img" aria-label="Runner on a stadium track before a packed crowd at night" style="left:187px;top:91px;width:148px;height:69px;border-radius:8px;background:linear-gradient(180deg,#1d2c55,#4f6ea5 45%,#a8733f 75%,#c99a5f)"></div>
  <div class="block heading" style="left:22px;top:147px;font-size:11.5px">THE FINISH LINE</div>
  <div class="block" style="left:22px;right:22px;top:166px">
    <p>Jesus himself defined the finish line when he said, “This gospel of the kingdom will be preached in the whole world as a testimony to all nations, and then the end will come.”</p>
  </div>
  <div class="grey-band" style="top:191px;height:40px;text-align:center;font:500 8px/1.45 'Oswald',sans-serif;color:#222;padding-top:7px">WHEN WILL THE RACE END?<br>JESUS SAID, WHEN THE GOSPEL HAS BEEN PROCLAIMED TO “ALL NATIONS.”</div>
  <div class="block" style="left:22px;right:22px;top:240px">
    <p>In the Bible, the word “nations” refers to people groups: groups of people who share a common ethnicity, culture, and language. Amazingly, there are about 12,000 of these “nations” around the world—and Jesus commanded His disciples in all of them!</p>
    <p>Today, there are still about 500 people groups around the world who have never heard the gospel. Most of these remaining groups are small and located in remote, difficult places. But now that we know who and where they are, by God’s grace it is possible for us to engage every one of them with the gospel within the next 3 years.</p>
  </div>
  <div class="photo" role="img" aria-label="Sprinter leaning toward the finish line" style="left:24px;top:297px;width:82px;height:36px;border-radius:5px;background:linear-gradient(90deg,#b8543a,#8c3a2a 50%,#c77a55)"></div>
  <div class="block" style="left:114px;right:20px;top:299px">
    <div class="heading" style="font-size:11px;margin-bottom:3px">SPRINTING TO THE FINISH</div>
    <p>In his second letter, the Apostle Peter instructs believers “to hasten the coming of the day of God.” As the end of the race draws near, he’s saying, we should sprint toward the finish line, striving to finish the race as quickly as we can.</p>
  </div>
  <div class="cta" style="top:373px;height:43px;padding-top:9px">
    <div class="cta-label"><i class="rule l"></i><span>YOU CAN BE PART OF THE SPRINT TO THE FINISH</span><i class="rule r"></i></div>
    <p>Partner with Harvest Reach Partners and finance the missionaries who are taking the gospel for the first time to those last remaining people groups. Your investment will “hasten the coming of the day of God” by accelerating the effort to make “disciples in every nation.” In 2018, our partners helped take the gospel to 231 people groups in 35 countries.</p>
  </div>
  <div class="footer"><div class="brand"><div class="brand-mark"></div><div class="brand-name">Harvest Reach Partners</div></div><div class="contact"><small>To learn more, email Martin Hale at</small><a>mhale@harvestreach.org.</a></div></div>
  <div class="pill">Join us as we invest to make disciples in “all nations” by 2022</div>
</section>

</body>
</html>
```